Pivots & Treads .com

This website is simple!!!
Landing page background image should capture the customers attention!!! We will provide a image as a example of what we like. The purpose for this website is to provide customers with a clean easy way to request a quote for industrial casters and wheels by OEM’s as well as maintenance departments worldwide. Please see if you can follow our thought process below.
Customer comes to website, they are invited to Request a Quote by providing us with Manufacturer Name, Manufacturers Part # and quantity needed.
If this is not known the customer will complete will WP conversation format form answering about 10 questions
Or
Look up the part number in one of the 8 to 12 catalogs located in the Flippin Book format on our catalog page, or equal plug in .
When the client request a quote a account page will pop up request The following:
Clients first and last name
Email address
And optional questions
Company name and best contact number.
Once this is complete customer will hit SUBMIT.
The customers request will be in system. A email will be sent to Customer service notifying us the Quote Request has been made.
We will then build a quote for the customer with a good, better and best options. Customers Request a Quote submission may have more than one caster or wheel requested at a time, so website must allow this.
When the customer comes back into website there email address will come up as the account name and request a password be made for them. This will allow them to store quotes in their account for future needs. If quote is older than 30 day the system will trigger a button at the bottom of the quote for resubmit Request for updated quote.
Once customer reviews quote the quote can be Converted to order within the website.
Once Converted the system will send us a email and order will be processed.
We will need a Chat program that will text to CS the questions.
You will need to have high quality graphic design skills on your team.
We have found 2 plugins that would work nicely with our new website Flippin books to showcase our catalogs for customers to research and WPForms conversation forms to complete request for quote form.
Just Ideas:
Very very ghosted caster blueprint in white background but very very ghosted or the icon just idea
We have never had a font used we like
Grayscale every except for rubber on wheels and logo icon
Website should have hamburger menu on left
Website should hav responsive deign
Account head on right side
Has anyone read the brief from top to bottom and the updates, I’m seeing a lot of duplicates of the website I posted in images I want a clean website With lite backgrand with the poly being definite colors on each wheel I added a green yellow and red image has anyone looked at that Just a question?
Went on vacation/holiday

```html
<!DOCTYPE html>
<html lang="en">
<head>
<meta charset="UTF-8">
<title>Pivots &amp; Treads .com — Request a Quote</title>
<link rel="stylesheet" href="https://fonts.googleapis.com/css2?family=Montserrat:wght@500;600;700;800&family=Poppins:wght@400;500;600;700&display=swap">
<style>
  :root {
    --brand-blue: #27479a;
    --ink: #111111;
    --charcoal: #34373b;
    --steel: #5c5e61;
    --white: #ffffff;
    --hero-light: #f1f1f1;
    --hero-mid: #d9d9d9;
    --footer-text: #8d8f93;
  }
  * { box-sizing: border-box; margin: 0; padding: 0; }
  html, body { width: 1200px; height: 768px; overflow: hidden; background: var(--white); }
  .page {
    position: relative; width: 1200px; height: 768px; overflow: hidden;
    font-family: "Montserrat", sans-serif; color: var(--ink);
  }

  /* Header */
  .site-header { position: absolute; inset: 0 0 auto 0; height: 104px; background: var(--white); z-index: 3; }
  .contact-band { position: absolute; top: 0; left: 0; width: 1200px; height: 41px; }
  .contact-list {
    position: absolute; top: 9px; left: 692px; display: flex; align-items: center;
    font-family: "Poppins", sans-serif; font-size: 15px; color: var(--white);
  }
  .contact-item { display: flex; align-items: center; gap: 10px; }
  .contact-divider { width: 1px; height: 18px; background: #bfc0c2; margin: 0 30px; }

  .menu-toggle {
    position: absolute; left: 80px; top: 49px; display: flex; align-items: center; gap: 8px;
    font-family: "Poppins", sans-serif; font-weight: 600; font-size: 14px; letter-spacing: .3px; color: var(--ink);
  }
  .menu-bars { display: flex; flex-direction: column; gap: 4px; }
  .menu-bars span { display: block; width: 26px; height: 2.5px; background: var(--ink); }

  .brand {
    position: absolute; left: 190px; top: 36px; display: flex; align-items: center; gap: 12px;
    font-family: "Montserrat", sans-serif; font-weight: 700; font-size: 23px; color: var(--brand-blue);
  }
  .brand-dot { width: 44px; height: 44px; border-radius: 50%; background: var(--brand-blue); }

  .account-link {
    position: absolute; right: 98px; top: 62px; display: flex; align-items: center; gap: 8px;
    font-family: "Poppins", sans-serif; font-weight: 600; font-size: 14px; letter-spacing: .3px; color: var(--ink);
    text-decoration: none;
  }

  /* Hero */
  .hero-backdrop {
    position: absolute; top: 104px; left: 0; width: 1200px; height: 580px;
    background: radial-gradient(ellipse at 55% 45%, var(--hero-light) 0%, #e6e6e6 55%, var(--hero-mid) 100%);
  }
  .product-shot {
    position: absolute; left: 596px; top: 233px; width: 512px; height: 336px;
    background:
      radial-gradient(closest-side at 26% 58%, #3558aa 0%, #6f86bf 45%, #c9ccd1 75%, rgba(230,230,230,0) 100%),
      radial-gradient(closest-side at 76% 66%, #3558aa 0%, #6f86bf 45%, #c9ccd1 75%, rgba(230,230,230,0) 100%);
    background-repeat: no-repeat;
  }
  .hero-copy { position: absolute; left: 80px; top: 196px; z-index: 2; }
  .eyebrow {
    display: flex; align-items: center; gap: 12px;
    font-weight: 500; font-size: 26px; letter-spacing: .5px; color: var(--ink);
  }
  .eyebrow-line { width: 44px; height: 2px; background: var(--steel); position: relative; }
  .eyebrow-line::after { content: ""; position: absolute; right: 0; top: -4px; width: 2px; height: 10px; background: var(--steel); }
  .headline {
    margin-top: 2px; font-weight: 800; font-size: 62px; line-height: 71px; letter-spacing: .5px; color: var(--ink);
  }
  .steps { display: flex; align-items: center; margin-top: 4px; }
  .steps-label { font-size: 20px; font-weight: 500; margin-right: 15px; }
  .step-track { position: relative; display: flex; gap: 11px; }
  .step-track::before {
    content: ""; position: absolute; left: 20px; right: 20px; top: 19px; height: 4px; background: var(--white);
  }
  .step {
    position: relative; width: 42px; height: 42px; border-radius: 50%; background: var(--white);
    display: flex; align-items: center; justify-content: center;
    font-family: "Poppins", sans-serif; font-weight: 700; font-size: 20px; color: var(--ink);
    box-shadow: 0 1px 4px rgba(0,0,0,.12);
  }
  .process-list { list-style: none; margin-top: 18px; display: flex; flex-wrap: wrap; width: 420px; row-gap: 18px; column-gap: 16px; }
  .process-item { display: flex; align-items: center; gap: 10px; font-size: 18px; font-weight: 500; color: #1d1d1d; }
  .process-item svg { flex: none; }
  .actions { display: flex; gap: 17px; margin-top: 28px; }
  .btn {
    display: flex; align-items: center; justify-content: center; gap: 8px; height: 50px; border-radius: 25px;
    font-family: "Poppins", sans-serif; font-weight: 600; font-size: 15px; letter-spacing: .5px; color: var(--white);
    text-decoration: none;
  }
  .btn-quote { width: 239px; background: var(--brand-blue); }
  .btn-catalog { width: 174px; background: var(--charcoal); }

  /* Footer */
  .site-footer { position: absolute; left: 0; top: 645px; width: 1200px; height: 123px; }
  .site-footer svg { position: absolute; inset: 0; }
  .copyright {
    position: absolute; top: 68px; width: 100%; text-align: center;
    font-family: "Poppins", sans-serif; font-size: 16px; color: var(--footer-text);
  }
</style>
</head>
<body>
<div class="page">

  <header class="site-header">
    <svg class="contact-band" viewBox="0 0 1200 41" aria-hidden="true">
      <polygon points="513,0 1200,0 1200,41 672,41 660,4 516,4" fill="#34373b"/>
    </svg>
    <div class="contact-list">
      <span class="contact-item">
        <svg width="17" height="17" viewBox="0 0 24 24" aria-hidden="true"><path fill="#fff" d="M6.6 10.8a15.1 15.1 0 0 0 6.6 6.6l2.2-2.2a1 1 0 0 1 1-.25 11.4 11.4 0 0 0 3.6.57 1 1 0 0 1 1 1V20a1 1 0 0 1-1 1A17 17 0 0 1 3 4a1 1 0 0 1 1-1h3.5a1 1 0 0 1 1 1c0 1.25.2 2.45.57 3.57a1 1 0 0 1-.25 1z"/></svg>
        555-014-2290
      </span>
      <span class="contact-divider"></span>
      <span class="contact-item">
        <svg width="19" height="17" viewBox="0 0 24 22" aria-hidden="true"><path fill="#fff" d="M12 1 2 7.5V20a1 1 0 0 0 1 1h18a1 1 0 0 0 1-1V7.5zm0 11L4.5 7.6 12 3l7.5 4.6z"/></svg>
        info@pivotstreads.com
      </span>
    </div>

    <div class="menu-toggle">
      <span class="menu-bars"><span></span><span></span><span></span></span>
      MENU
    </div>

    <div class="brand">
      <span class="brand-dot"></span>
      <span>PIVOTS &amp; TREADS.com</span>
    </div>

    <a class="account-link" href="#">
      <svg width="18" height="18" viewBox="0 0 20 20" aria-hidden="true"><circle cx="10" cy="6" r="4" fill="#111"/><path d="M2 19c0-4.4 3.6-7 8-7s8 2.6 8 7z" fill="#111"/></svg>
      ACCOUNT
    </a>
  </header>

  <main>
    <div class="hero-backdrop" role="img" aria-label="Soft grey textured wall with faint handprints behind the hero"></div>
    <div class="product-shot" role="img" aria-label="Two chrome swivel casters with blue polyurethane wheels"></div>

    <section class="hero-copy">
      <p class="eyebrow">SOLUTIONS FOR <span class="eyebrow-line"></span></p>
      <h1 class="headline">ALL YOUR<br>APPLICATIONS</h1>

      <div class="steps">
        <span class="steps-label">Easy as :</span>
        <div class="step-track">
          <span class="step">1</span><span class="step">2</span><span class="step">3</span>
        </div>
      </div>

      <ul class="process-list">
        <li class="process-item"><svg width="18" height="18" viewBox="0 0 20 20" aria-hidden="true"><circle cx="10" cy="10" r="10" fill="#111"/><path d="M5 10h8M10 6l4 4-4 4" stroke="#fff" stroke-width="2.2" fill="none" stroke-linecap="round" stroke-linejoin="round"/></svg>Request a Quote</li>
        <li class="process-item"><svg width="18" height="18" viewBox="0 0 20 20" aria-hidden="true"><circle cx="10" cy="10" r="10" fill="#111"/><path d="M5 10h8M10 6l4 4-4 4" stroke="#fff" stroke-width="2.2" fill="none" stroke-linecap="round" stroke-linejoin="round"/></svg>Receive a Quote</li>
        <li class="process-item"><svg width="18" height="18" viewBox="0 0 20 20" aria-hidden="true"><circle cx="10" cy="10" r="10" fill="#111"/><path d="M5 10h8M10 6l4 4-4 4" stroke="#fff" stroke-width="2.2" fill="none" stroke-linecap="round" stroke-linejoin="round"/></svg>Convert a Quote to order</li>
      </ul>

      <div class="actions">
        <a class="btn btn-quote" href="#">REQUEST A QUOTE
          <svg width="15" height="14" viewBox="0 0 16 14" aria-hidden="true"><path d="M1 7h12M8 2l5 5-5 5" stroke="#fff" stroke-width="2.4" fill="none" stroke-linecap="round" stroke-linejoin="round"/></svg>
        </a>
        <a class="btn btn-catalog" href="#">CATALOG
          <svg width="19" height="15" viewBox="0 0 20 16" aria-hidden="true"><path fill="#fff" d="M1 1.5c3-.6 6 0 8.2 1.5V15C7 13.6 4 13 1 13.6zM19 1.5c-3-.6-6 0-8.2 1.5V15c2.2-1.4 5.2-2 8.2-1.4z"/></svg>
        </a>
      </div>
    </section>
  </main>

  <footer class="site-footer">
    <svg viewBox="0 0 1200 123" aria-hidden="true">
      <rect x="0" y="36" width="1200" height="87" fill="#34373b"/>
      <polygon points="0,18 89,18 121,53 0,53" fill="#34373b"/>
      <polygon points="1200,18 1111,18 1079,53 1200,53" fill="#34373b"/>
      <polygon points="0,0 100,0 132,36 222,36 222,53 120,53 89,18 0,18" fill="#5c5e61"/>
      <polygon points="1200,0 1100,0 1068,36 978,36 978,53 1080,53 1111,18 1200,18" fill="#5c5e61"/>
    </svg>
    <p class="copyright">Copyright © 2022 Pivots &amp; Treads All rights reserved.</p>
  </footer>

</div>
</body>
</html>
```